Tallwood Ridge firewood

It a new firewood outlet in Jindabyne nsw that will only sell top hardwood firewood (ironbark , red gum, grey gum, an box mix. I would like to see a web page the we can do order online payment for delivery. It will all so need to have photos of the firewood. I all so have logo for tallwood ridge firewood
Must have a modem look but easy to use I would like to see a black back ground of some sort.

Here are some other firewood web pages for ideas and firewood info
http://www.kestrelburnfuel.com.au
http://www.brindlefirewood.com.au
http://www.coppertonfirewood.com.au
http://www.wattleyhearthlogs.com.au/firewood

```html
<!DOCTYPE html>
<html lang="en">
<head>
<meta charset="utf-8">
<title>Tallwood Ridge Firewood</title>
<link href="https://fonts.googleapis.com/css2?family=Open+Sans:wght@400;700&display=swap" rel="stylesheet">
<style>
  :root {
    --page-bg: #4a3b32;
    --nav-bg: #778b9c;
    --heading: #b9d3ec;
    --text: #f4efe9;
    --tag-bg: rgba(70, 62, 58, 0.55);
    --logo-panel: rgba(236, 226, 214, 0.55);
    --logo-text: #5c4a3c;
    --wood-light: #caa17a;
    --wood-mid: #a87752;
    --wood-dark: #6e4a30;
  }
  html, body {
    margin: 0;
    padding: 0;
    width: 1200px;
    height: 687px;
    overflow: hidden;
    background: var(--page-bg);
    font-family: "Open Sans", Arial, sans-serif;
    color: var(--text);
  }
  .site-header {
    position: relative;
    height: 209px;
  }
  .header-photo {
    position: absolute;
    inset: 0;
    background:
      radial-gradient(ellipse 180px 130px at 540px 110px, var(--wood-light), transparent 70%),
      radial-gradient(ellipse 160px 120px at 820px 150px, var(--wood-light), transparent 70%),
      radial-gradient(ellipse 140px 110px at 1120px 140px, var(--wood-light), transparent 70%),
      linear-gradient(120deg, var(--wood-mid), var(--wood-dark) 45%, var(--wood-mid) 70%, var(--wood-dark));
  }
  .logo-panel {
    position: absolute;
    left: 109px;
    top: 0;
    width: 240px;
    height: 209px;
    background: var(--logo-panel);
    display: flex;
    flex-direction: column;
    align-items: center;
    justify-content: center;
    gap: 14px;
  }
  .logo-mark {
    width: 120px;
    height: 120px;
    border: 5px solid var(--logo-text);
    border-radius: 50%;
    box-sizing: border-box;
  }
  .logo-name {
    font-weight: 700;
    font-size: 17px;
    color: var(--logo-text);
    text-transform: uppercase;
    letter-spacing: 0.2px;
  }
  .header-contact {
    position: absolute;
    right: 112px;
    top: 36px;
    display: flex;
    flex-direction: column;
    align-items: flex-end;
  }
  .header-contact span {
    background: var(--tag-bg);
    color: #fff;
    padding: 0 3px;
  }
  .phone {
    font-weight: 700;
    font-size: 33px;
    line-height: 44px;
  }
  .address-line {
    font-size: 14px;
    line-height: 19.5px;
  }
  .site-main {
    display: flex;
    gap: 22px;
    padding: 25px 109px 0;
  }
  .main-nav {
    flex: 0 0 240px;
    height: 186px;
    background: var(--nav-bg);
    box-sizing: border-box;
    padding: 16px 15px 0 0;
  }
  .main-nav ul {
    list-style: none;
    margin: 0;
    padding: 0;
    text-align: right;
  }
  .main-nav li {
    font-size: 15.3px;
    line-height: 21.8px;
  }
  .main-nav a {
    color: #fff;
    text-decoration: none;
  }
  .main-nav .current {
    font-weight: 700;
  }
  .content {
    width: 720px;
  }
  .content h1 {
    margin: 0 0 13px;
    color: var(--heading);
    font-size: 26px;
    line-height: 34px;
    font-weight: 700;
  }
  .content p {
    margin: 0 0 21.8px;
    font-size: 14.6px;
    line-height: 21.8px;
  }
  .content .intro {
    font-weight: 700;
    color: #fff;
  }
</style>
</head>
<body>
  <header class="site-header">
    <div class="header-photo" role="img" aria-label="Photo of stacked cut hardwood log ends"></div>
    <div class="logo-panel">
      <div class="logo-mark"></div>
      <div class="logo-name">Tallwood Ridge Firewood</div>
    </div>
    <div class="header-contact">
      <span class="phone">024 76 555 018</span>
      <span class="address-line">Tallwood Ridge Firewood</span>
      <span class="address-line">14 Stringybark Lane</span>
      <span class="address-line">Jindabyne</span>
    </div>
  </header>

  <main class="site-main">
    <nav class="main-nav">
      <ul>
        <li><a class="current" href="#">Home</a></li>
        <li><a href="#">Products</a></li>
        <li><a href="#">Order</a></li>
        <li><a href="#">About Us</a></li>
        <li><a href="#">Contact Us</a></li>
        <li><a href="#">Page Title</a></li>
        <li><a href="#">Another Page</a></li>
      </ul>
    </nav>
    <section class="content">
      <h1>Welcome to Tallwood Ridge Firewood</h1>
      <p class="intro">Ne eius aliquip periculis has, has iriure quaeque detraxit ne. Sit libris minimum ei, mei habemus suscipiantur te. Vel ut erat repudiare, accumsan albucius vix id, ex pro noster aeterno tritani. Vix sale tation quaerendum cu, pri et quot veniam soluta. Quo ea accumsan torquatos, at has soluta fabulas. Et novum vivendo efficiendi nam.</p>
      <p>Lorem ipsum dolor sit amet, est ei stet sententiae. Graeci phaedrum tincidunt eum ea, pri alterum deserunt at. Hendrerit pertinacia vix et, eum at elit solet atomorum, eum te nusquam mandamus. Pro id verear detracto mandamus, nihil aliquip accusata vis eu, his et quot possit veritus. Tibique accusamus qui in, at vel diceret evertitur assentior, maluisset interesset ullamcorper pri ei.</p>
      <p>Ut iracundia inciderint eam, no eam periculis consulatu. Ut cum primis pertinax, est prima nominavi mediocrem ea. Consul partiendo in vim, no deserunt constituto sea. At pri persius insolens, cum in dicat percipitur. Natum appareat sententiae vim ad, qui cu aliquid euripidis prodesset.</p>
    </section>
  </main>
</body>
</html>
```